www.vandrik.com Sales/Order Page ReDesign

We need a new and amazing design for our sales/order page to attract more costumers and new houses for our portal.

Here is the existing page with the current design: https://www.vandrik.com/sales

We are proud owners of www.hyttetun.no and www.vandrik.com and we want more holiday home owners to join our page so that we can rent out their holiday homes and increase the number of houses on our portal.

To get more homeowners we need a sales page that can sell our products the best way possible. Therefore we want you too blow us away with a fresh, modern, easy understandable and stylish new sales/order page.

The only restrictions we give when it comes to design is that it needs to fit the existing design of our portals, the top and footer are set. Beside that we are open for everything as long as it at once give the customers impression that this is a good, professional page were they just have to put out their houses.

When it comes to content I have added two documents who include the content to put in here and some guidelines on how to organize the page. Please be creative and add necessary graphics, symbols, background pictures and what ever necessary to make this page look professional and appealing to new costumers.

Looking forward to what suggestions we are given.
Updates

We just want to inform that we have updated our brief with a much more concrete description of what content to add on the sale page, and who to structure the content on the page. Hope this helps to make suggestions easier. Looking forward to receive some good contributions.

We would just like to make sure that everyone have understood that we are not asking for a new design suggestion to our portal in general. We are only asking for a redesign of our sales/order page you find here www.vandrik.com/sales. We have to day received some designs for our front page and the design it self was good, but that's not what we are asking for this time and don't want you to use time of something we don't need at the moment. We are looking forward too se some good suggestions.

Project Deadline Extended
Reason: Hello. Thanks for all the great contributions we have been given so fare. We haven't been able to respond to all design and are therefore extending the deadline so that we are able to respond to the designs we have been giver and to gov time to make final changes.

Project Deadline Extended
Reason: We are extending the deadline to give designers time to give new suggestion based on our latest feedback today.

Project Deadline Extended
Reason: Extended so we can receive last design changes.

Target Market(s)

This is a presentation page where we present our product agains new home owner who we what to choose listing there property on or site.

Industry/Entity Type

Sales

Requirements
Must have
• A modern design who calms the costumer down and help them in deciding to chose us, and for them to choose us they need to trust and believe in us. Therefore your main task is to create a page that effectively informs about our product, gets the visitors attentions and make them trust us.
Nice to have
• Examples of good competitors and good order pages we like:

http://www.stayplume.com/info/lyp?icid=IL___O_Text___top_nav_link
https://www.nestorly.com/rooms/new
https://www.quince.com/tablo/compare/
http://www.lodgewick.com/host
Should not have
• - Bad design :-). With bad design we mean design that looks like it's made in 2 seconds by a little child.

```html
<!DOCTYPE html>
<html lang="en">
<head>
<meta charset="utf-8">
<title>Vandrik – List Your Properties</title>
<link rel="stylesheet" href="https://fonts.googleapis.com/css2?family=Noto+Serif:wght@400;700&family=Open+Sans:wght@400;600;700&display=swap">
<style>
:root{
  --navy:#1d3f6e;
  --blue:#1f7fd0;
  --sky:#3aa0e8;
  --title:#2a2a2a;
  --text:#555;
  --muted:#8a8a8a;
  --panel:rgba(255,255,255,.9);
  --box:#eeeeee;
  --line:#d9d9d9;
  --footer:#1a88d6;
  --orange:#f39a1f;
  --red:#e0463b;
  --green:#3fae4a;
  --purple:#7a4fb5;
  --teal:#1fa7a0;
  --dark:#3b3b3b;
}
*{box-sizing:border-box;margin:0;padding:0}
html,body{width:1200px;height:3776px;overflow:hidden}
body{position:relative;font-family:"Open Sans",Arial,sans-serif;color:var(--text);background:#cfe3f1}
.backdrop{position:absolute;inset:0;background:linear-gradient(180deg,#a9cbe6 0%,#d7e3ea 18%,#b9a98e 38%,#8fb7cf 55%,#c9b48f 72%,#9cc4db 88%,#b3cfe2 100%)}
.site-header{position:absolute;top:0;left:0;width:1200px;height:100px;background:#fff;border-top:6px solid var(--navy);box-shadow:0 2px 6px rgba(0,0,0,.15)}
.brand{position:absolute;left:150px;top:0;width:200px;height:94px;background:var(--navy);display:flex;align-items:center;justify-content:center;gap:10px}
.brand-mark{width:16px;height:16px;background:#fff}
.brand-name{font-family:"Noto Serif",Georgia,serif;font-weight:700;font-size:32px;color:#fff}
.header-tools{position:absolute;right:130px;top:12px;display:flex;align-items:center;gap:12px}
.lang{width:22px;height:14px;background:#cfd8e3}
.advert{background:var(--navy);color:#fff;font-size:13px;padding:6px 12px;border-radius:3px}
.list-btn{background:var(--sky);color:#fff;font-size:13px;font-weight:600;padding:6px 14px;border-radius:3px}
.panel{position:absolute;left:125px;top:125px;width:950px;height:3130px;background:var(--panel);box-shadow:0 0 12px rgba(0,0,0,.15)}
.intro-title{position:absolute;top:42px;left:0;width:100%;text-align:center;font-family:"Noto Serif",Georgia,serif;font-weight:700;font-size:22px;line-height:30px;color:var(--title)}
.intro-lead{position:absolute;top:84px;left:25px;width:900px;text-align:center;font-family:"Noto Serif",Georgia,serif;font-size:22px;line-height:34px;color:var(--blue)}
.intro-sub{position:absolute;top:164px;left:0;width:100%;text-align:center;font-family:"Noto Serif",Georgia,serif;font-size:22px;line-height:30px;color:var(--blue)}
.hero-photo{position:absolute;top:212px;left:35px;width:880px;height:460px;background:linear-gradient(180deg,#3d86d6 0%,#8fc3ef 40%,#7a5a45 55%,#3f7a2f 75%,#2f6626 100%);box-shadow:0 8px 14px rgba(0,0,0,.25)}
.profit{position:absolute;top:708px;left:0;width:100%;text-align:center;font-family:"Noto Serif",Georgia,serif;font-size:24px;line-height:34px;color:var(--blue)}
.benefits{position:absolute;top:815px;left:60px;width:830px;display:grid;grid-template-columns:1fr 1fr;column-gap:60px;row-gap:38px}
.benefit{display:flex;gap:16px}
.icon{flex:none;width:44px;height:44px;border-radius:50%;display:flex;align-items:center;justify-content:center}
.benefit h3,.service h3{font-size:15px;font-weight:700;color:var(--title);margin-bottom:4px}
.benefit p{font-size:12.5px;line-height:18px;color:var(--text)}
.help-box{position:absolute;top:1072px;left:60px;width:830px;height:378px;background:var(--box);border:1px solid var(--line);display:flex}
.manager{width:470px;padding:28px 34px;border-right:1px solid var(--line);text-align:center}
.manager h3,.contact h3{font-size:15px;font-weight:700;color:var(--title)}
.team-photo{margin:18px auto;width:170px;height:110px;background:linear-gradient(135deg,#cfd9e4,#8ea6bf)}
.manager p{font-size:12.5px;line-height:19px;text-align:center}
.contact{flex:1;padding:28px 30px;text-align:center}
.contact .icon{margin:40px auto 10px}
.contact .phone{font-size:24px;color:var(--title)}
.contact .mail{font-size:14px;color:var(--blue);text-decoration:underline}
.services-title{position:absolute;top:1512px;left:0;width:100%;text-align:center;font-family:"Noto Serif",Georgia,serif;font-weight:700;font-size:24px;color:var(--blue)}
.services{position:absolute;top:1570px;left:60px;width:830px;list-style:none}
.service{display:flex;gap:22px;align-items:flex-start;height:122px;padding-top:26px;border-bottom:1px solid var(--line)}
.service p{font-size:12.5px;line-height:18px}
.closing{position:absolute;top:2980px;left:0;width:100%;text-align:center;font-family:"Noto Serif",Georgia,serif;font-size:24px;color:var(--blue)}
.site-footer{position:absolute;top:3265px;left:0;width:1200px;height:511px;background:var(--footer);color:#fff;border-top:8px solid var(--navy)}
.footer-cols{position:absolute;top:50px;left:130px;width:940px;display:flex;gap:40px}
.footer-col h4{font-size:15px;font-weight:700;margin-bottom:10px}
.footer-col li{list-style:none;font-size:13px;line-height:22px}
.world-map{width:220px;height:120px;background:linear-gradient(135deg,rgba(255,255,255,.55),rgba(255,255,255,.3));border-radius:6px}
</style>
</head>
<body>
<div class="backdrop" role="img" aria-label="Background photo of a sunny beach with palm trees and blue sea"></div>

<header class="site-header">
  <div class="brand"><span class="brand-mark"></span><span class="brand-name">Vandrik</span></div>
  <div class="header-tools">
    <span class="lang"></span><span class="lang"></span><span class="lang"></span>
    <span class="advert">Advertising your properties?</span>
    <span class="list-btn">List your property</span>
  </div>
</header>

<main class="panel">
  <h1 class="intro-title">Do You Own or Manage More Then 5 Properties ?</h1>
  <p class="intro-lead">Then we both want and are ready to help you maximize your profit on your<br>portfolio and to help to make the administration of it more efficient.</p>
  <p class="intro-sub">On Vandrik you can rent out:</p>
  <div class="hero-photo" role="img" aria-label="Photo of a red brick castle with towers beside a moat and green lawn"></div>
  <p class="profit">And make a profit on it. You ask how?<br>Keep reading and we will let you know how easy and hassle free it is!</p>

  <section class="benefits">
    <div class="benefit"><span class="icon" style="background:var(--dark)"><svg width="20" height="20"><circle cx="10" cy="10" r="7" fill="none" stroke="#fff" stroke-width="2"/></svg></span><div><h3>Good Exposure</h3><p>List online to a wide network of partners.</p></div></div>
    <div class="benefit"><span class="icon" style="background:var(--orange)"><svg width="20" height="20"><rect x="3" y="5" width="14" height="10" fill="none" stroke="#fff" stroke-width="2"/></svg></span><div><h3>Flexible Payment Plans</h3><p>Whether you prefer to pay commission or a yearly fee, we have a plan that suits your listing needs.</p></div></div>
    <div class="benefit"><span class="icon" style="background:var(--dark)"><svg width="20" height="20"><rect x="5" y="9" width="10" height="8" fill="#fff"/><path d="M7 9V6a3 3 0 0 1 6 0v3" fill="none" stroke="#fff" stroke-width="2"/></svg></span><div><h3>Secure Online Booking</h3><p>Tenants book and pay online, so you get paid safely and keep full control of your calendar.</p></div></div>
    <div class="benefit"><span class="icon" style="background:var(--orange)"><svg width="20" height="20"><path d="M4 10l4 4 8-8" fill="none" stroke="#fff" stroke-width="2.5"/></svg></span><div><h3>Easy to Get Started &amp; Updated</h3><p>We can import your listings with an XML feed, or you add them yourself with our simple tools.</p></div></div>
  </section>

  <section class="help-box">
    <div class="manager">
      <h3>Dedicated Account Manager</h3>
      <div class="team-photo" role="img" aria-label="Photo of a business team at work"></div>
      <p>You will have one contact person who will be your direct contact with us. Our team supports you with marketing, holiday listings around the world and is glad to share their expertise with you. Your personal account manager will help you get the highest return on your investment.</p>
    </div>
    <div class="contact">
      <h3>Contact Us If You Need Help to List</h3>
      <span class="icon" style="background:var(--navy)"><svg width="20" height="20"><rect x="6" y="2" width="8" height="16" rx="2" fill="none" stroke="#fff" stroke-width="2"/></svg></span>
      <p class="phone">+ 47 41 52 63 74</p>
      <span class="icon" style="background:var(--navy)"><svg width="20" height="20"><rect x="2" y="5" width="16" height="11" fill="none" stroke="#fff" stroke-width="2"/><path d="M2 5l8 6 8-6" fill="none" stroke="#fff" stroke-width="2"/></svg></span>
      <p class="mail">property@vandrik.com</p>
    </div>
  </section>

  <h2 class="services-title">All Our Announcements Have The Following Services Included:</h2>
  <ul class="services">
    <li class="service"><span class="icon" style="background:var(--sky)"></span><div><h3>Access Scandinavians</h3><p>Our rentals are found across Norway, and we reach travellers all over the Scandinavian market, with many well paying guests from these strong demographics.</p></div></li>
    <li class="service"><span class="icon" style="background:var(--orange)"></span><div><h3>Broad Exposure</h3><p>We have been on the market for several years and are promoting your property through the necessary and right channels.</p></div></li>
    <li class="service"><span class="icon" style="background:var(--red)"><svg width="20" height="20"><path d="M4 10l4 4 8-8" fill="none" stroke="#fff" stroke-width="2.5"/></svg></span><div><h3>Trust &amp; Safety</h3><p>You are still in control of your property. We have the tools to help you accept a booking only if you are 100% comfortable.</p></div></li>
    <li class="service"><span class="icon" style="background:var(--green)"></span><div><h3>No Traveler Fees</h3><p>Unlike many other vacation rental booking sites, travellers can book vacation rentals without paying any fees to us, so the rate you set is the rate they see.</p></div></li>
    <li class="service"><span class="icon" style="background:var(--navy)"></span><div><h3>Payments by Vandrik</h3><p>Guests are always careful when it comes to payment. Every booking is handled securely through our payment system. We are responsible for the payments.</p></div></li>
    <li class="service"><span class="icon" style="background:var(--teal)"></span><div><h3>Online Booking</h3><p>We simplify the booking process by allowing tenants to send online reservation requests, which gives you 24 hours to accept or decline them.</p></div></li>
    <li class="service"><span class="icon" style="background:var(--purple)"></span><div><h3>Easy to Use Tools</h3><p>Get access to a set of well developed reservation and management tools that help you keep track of bookings.</p></div></li>
    <li class="service"><span class="icon" style="background:var(--green)"></span><div><h3>Unlimited Inquiries</h3><p>When you are renting out your property you need inquiries, therefore we have no limits on inquiries for your property.</p></div></li>
    <li class="service"><span class="icon" style="background:var(--red)"></span><div><h3>Unlimited Photos</h3><p>A picture says more than 1000 words, therefore we let you upload as many pictures as possible.</p></div></li>
    <li class="service"><span class="icon" style="background:var(--orange)"></span><div><h3>Online Calendar</h3><p>Tenants like to know when your property is available straight away, and we let them know that. At the same time you can easily manage your availability.</p></div></li>
    <li class="service"><span class="icon" style="background:var(--dark)"><svg width="20" height="20"><path d="M10 18s-6-6-6-10a6 6 0 0 1 12 0c0 4-6 10-6 10z" fill="#fff"/></svg></span><div><h3>Map and Location</h3><p>Tenants are always wondering where your property is located. Show them through our map and let them know where nearby attractions are.</p></div></li>
  </ul>

  <p class="closing">We can't wait to also help you with getting more bookings for the future...</p>
</main>

<footer class="site-footer">
  <div class="footer-cols">
    <div class="footer-col"><h4>Destinations</h4><ul><li>Europe</li><li>North America</li><li>South America</li><li>Africa</li><li>Asia</li><li>Australia</li></ul></div>
    <div class="world-map" role="img" aria-label="World map outline"></div>
    <div class="footer-col"><h4>For tenants</h4><ul><li>My page</li><li>Why Vandrik</li><li>FAQ</li><li>Rental terms</li></ul></div>
    <div class="footer-col"><h4>For house owners</h4><ul><li>My page</li><li>List as rental owner</li><li>Conditions</li></ul></div>
    <div class="footer-col"><h4>Contact us</h4><ul><li>Vandrik Holiday Rental</li><li>property@vandrik.com</li><li>+47 41 52 63 74</li><li>www.vandrik.com</li><li><strong>Opening hours</strong></li><li>Mon - Fri: 9:00 - 15:00</li><li>Sat - Sun: Closed</li></ul></div>
  </div>
</footer>
</body>
</html>
```